Solids Control Presentation Template Design

I'm putting together a technical 5-day course about solids control and waste management. I'm looking for an updated art and a easy on the eyes format.

```html
<!DOCTYPE html>
<html lang="en">
<head>
<meta charset="utf-8">
<title>Gritline – Solids Control Presentation Template</title>
<link rel="stylesheet" href="https://fonts.googleapis.com/css2?family=Oswald:wght@300;400;500;700&family=Open+Sans:wght@400;600&display=swap">
<style>
:root{
  --red:#8c2f31;
  --red-mid:#a8494c;
  --red-soft:#c66a6c;
  --ink:#222426;
  --grey:#5d5f61;
  --night:#23272b;
  --page:#efefef;
  --stage:#e8e8e6;
  --white:#ffffff;
}
*{margin:0;padding:0;box-sizing:border-box}
html,body{width:1200px;height:3242px;overflow:hidden}
body{background:var(--page);position:relative;font-family:"Open Sans",Arial,sans-serif;color:var(--grey)}
.stage{position:absolute;left:0;top:0;width:1200px;height:800px;background:var(--stage)}
.hero{position:absolute;left:262px;top:170px;width:676px;height:380px;overflow:hidden;
  background:linear-gradient(180deg,#474d52 0%,#2a2f33 55%,#15181b 100%);box-shadow:0 10px 30px rgba(0,0,0,.25)}
.hero .band{position:absolute;left:0;right:0;top:134px;height:120px;background:rgba(255,255,255,.10);border-bottom:2px solid var(--red-mid)}
.hero .logo-box{position:absolute;left:28px;top:0;width:128px;height:52px;background:var(--white);display:flex;align-items:center;justify-content:center}
.hero h1{position:absolute;left:66px;top:140px;font-family:Oswald,sans-serif;font-weight:500;color:#fff;font-size:34px;letter-spacing:.5px}
.hero .sub{position:absolute;left:66px;top:184px;font-family:Oswald,sans-serif;font-weight:300;color:#fff;font-size:18px}
.hero .tags{position:absolute;left:66px;top:210px;font-family:Oswald,sans-serif;font-weight:300;color:#d6d6d6;font-size:12px}
.photo{position:absolute}
.mark{font-family:Oswald,sans-serif;font-weight:700;color:var(--red);letter-spacing:1.5px;font-size:12px;line-height:1}
.slide{position:absolute;width:560px;height:314px;overflow:hidden;background:var(--white);box-shadow:0 2px 6px rgba(0,0,0,.12)}
.c1{left:28px}.c2{left:616px}
.slide .mark.tr{position:absolute;right:12px;top:16px}
.foot{position:absolute;left:0;right:0;bottom:0;height:9px;background:var(--red);color:#fff;font-size:6px;text-align:right;padding-right:36px;line-height:9px}
.title{position:absolute;left:27px;top:14px;font-family:Oswald,sans-serif;font-weight:500;font-size:23px;color:var(--ink)}
.title::before{content:"";position:absolute;left:0;top:-6px;width:46px;height:3px;background:var(--red)}
.h{font-family:Oswald,sans-serif;font-weight:500;font-size:11px;color:var(--ink);margin-bottom:6px}
.p{font-size:7px;line-height:12px;color:var(--grey);text-align:justify}
.wt{color:#fff}
.ticks{list-style:none;font-size:7px;line-height:13px}
.ticks li::before{content:"✓";margin-right:5px}
.svc-h{font-family:Oswald,sans-serif;font-size:8px;margin-bottom:2px}
.svc-p{font-size:5.5px;line-height:7.5px;color:#fff;text-align:justify}
</style>
</head>
<body>

<section class="stage">
  <div class="hero">
    <div class="photo" role="img" aria-label="Dusk silhouette of an oil pumpjack over a field" style="inset:0;background:linear-gradient(160deg,rgba(90,96,102,.4),rgba(10,12,14,.4))"></div>
    <div class="band"></div>
    <div class="logo-box"><span class="mark" style="font-size:14px">GRITLINE</span></div>
    <h1>GRITLINE</h1>
    <div class="sub">Field Proven Methods</div>
    <div class="tags">Design – Advisory – Courses – Hardware</div>
  </div>
</section>

<!-- Row 1 -->
<article class="slide c1" style="top:824px;background:linear-gradient(180deg,#a5585a 0%,#8e3437 60%,#7d2527 100%)">
  <div class="photo" role="img" aria-label="Oil pumpjack silhouette under a cloudy sky, red toned" style="inset:0;background:linear-gradient(200deg,rgba(255,255,255,.08),rgba(0,0,0,.12))"></div>
  <div style="position:absolute;left:0;right:0;top:112px;text-align:center;color:#fff">
    <div style="width:30px;height:2px;background:#fff;margin:0 auto 10px"></div>
    <div style="font-family:Oswald,sans-serif;font-weight:300;font-size:11px">FIELD PROVEN METHODS</div>
    <div style="font-family:Oswald,sans-serif;font-weight:500;font-size:36px;line-height:44px;letter-spacing:1px">GRITLINE</div>
    <div style="display:inline-block;border:1px solid rgba(255,255,255,.5);padding:2px 16px;font-family:Oswald,sans-serif;font-weight:300;font-size:9px">Design – Advisory – Courses – Hardware</div>
  </div>
</article>

<article class="slide c2" style="top:824px">
  <div class="photo" role="img" aria-label="Oil pumpjack on the horizon, red toned" style="left:0;top:0;width:560px;height:144px;background:linear-gradient(180deg,#b56a6b,#93393c)"></div>
  <span class="mark" style="position:absolute;left:28px;top:194px;font-size:17px">GRITLINE</span>
  <div style="position:absolute;left:182px;top:186px;width:1px;height:36px;background:#ccc"></div>
  <div style="position:absolute;left:198px;top:188px;font-family:Oswald,sans-serif;font-weight:500;font-size:19px;color:var(--ink)">Title of presentation goes here</div>
  <div style="position:absolute;left:202px;top:218px;font-size:6px;color:#999">November 2019</div>
  <div class="foot"></div>
</article>

<!-- Row 2 -->
<article class="slide c1" style="top:1167px;background:linear-gradient(90deg,#1b1d20,#34393d 70%,#2c3034)">
  <div class="photo" role="img" aria-label="Silhouettes of a drilling rig and two workers shaking hands" style="inset:0;background:linear-gradient(180deg,rgba(80,86,92,.3),rgba(0,0,0,.5))"></div>
  <div style="position:absolute;left:0;width:560px;top:106px;height:90px;background:rgba(255,255,255,.06)"></div>
  <div style="position:absolute;right:26px;top:0;width:116px;height:48px;background:#fff;display:flex;align-items:center;justify-content:center"><span class="mark">GRITLINE</span></div>
  <div style="position:absolute;left:90px;top:94px;font-family:Oswald,sans-serif;font-weight:700;font-size:78px;line-height:80px;color:#c0474a">25</div>
  <div style="position:absolute;left:203px;top:106px;font-family:Oswald,sans-serif;font-size:14px;color:#d85a5c">YEARS OF EXPERIENCE</div>
  <div class="p wt" style="position:absolute;left:203px;top:134px;width:260px;font-size:7px;line-height:11px">Since 1994, GRITLINE has helped rig crews keep mud clean and waste low. Started in Tulsa, OK by field engineer Dan Hollister, the team now runs audits, site visits and hands-on courses across many basins.<br><br>Every instructor has spent years on location running shakers, centrifuges and dryers. We turn that time on the rig into clear lessons, lower haul-off volumes and better use of every piece of gear.</div>
</article>

<article class="slide c2" style="top:1167px;background:linear-gradient(135deg,#b25c5e,#8d3336)">
  <div class="photo" role="img" aria-label="Pumpjack at dusk, red toned" style="inset:0;background:linear-gradient(180deg,rgba(255,255,255,.06),rgba(0,0,0,.08))"></div>
  <div style="position:absolute;left:20px;top:104px;font-family:Oswald,sans-serif;font-weight:500;font-size:25px;line-height:28px;color:#fff">Our<br>Services</div>
  <div style="position:absolute;left:150px;top:34px;width:390px;display:grid;grid-template-columns:1fr 1fr;column-gap:20px;row-gap:10px;color:#fff">
    <div><div class="svc-h">▭ ENGINEERING</div><div class="svc-p">Layouts for tanks, shakers and centrifuges sized to each well plan, from first sketch to rig-up checks on site.</div></div>
    <div><div class="svc-h">⚙ CONSULTING</div><div class="svc-p">Reviews of fluid, solids and cuttings handling as one loop, with plain steps that lift uptime and trim spend.</div></div>
    <div><div class="svc-h">⚲ PROJECT MANAGEMENT</div><div class="svc-p">Planning and follow-up for multi-rig programs, keeping vendors, schedules and budgets lined up.</div></div>
    <div><div class="svc-h">○ TRAINING</div><div class="svc-p">Five-day classroom and yard courses on solids removal and waste handling for hands and supervisors.</div></div>
    <div><div class="svc-h">☝ APP DEVELOPMENT</div><div class="svc-p">Simple mobile logs and dashboards so daily solids data reaches the office without extra paperwork.</div></div>
    <div><div class="svc-h">◌ LAB ANALYSIS</div><div class="svc-p">Sample testing for mud, returns and waste streams, with short reports that point to the next fix.</div></div>
  </div>
  <div style="position:absolute;left:0;right:0;bottom:0;height:28px;background:#fff">
    <span class="mark" style="position:absolute;left:22px;top:9px">GRITLINE</span>
    <span style="position:absolute;right:30px;top:10px;font-size:6px;color:var(--ink)">https://www.gritline-inc.com</span>
  </div>
</article>

<!-- Row 3 -->
<article class="slide c1" style="top:1511px">
  <div class="photo" role="img" aria-label="Spiral notebook, pen and phone on a white desk" style="left:0;top:0;width:242px;height:302px;background:linear-gradient(160deg,#f4f4f4,#bdbdbd)"></div>
  <span class="mark tr">GRITLINE</span>
  <div style="position:absolute;left:167px;top:51px;width:393px;height:60px;background:var(--red)"></div>
  <div style="position:absolute;left:202px;top:66px;font-family:Oswald,sans-serif;font-weight:500;font-size:20px;color:#fff">Welcome Message</div>
  <div style="position:absolute;left:264px;top:130px;width:270px"><div class="h">Replace Your Text Here</div><div class="p">Duis arcu tortor, suscipit eget, imperdiet nec, imperdiet iaculis, ipsum. Sed aliquam ultrices mauris. Integer ante arcu, accumsan a, consectetuer eget, posuere ut, mauris. Praesent adipiscing. Phasellus ullamcorper. Duis arcu tortor, suscipit eget, imperdiet nec, imperdiet iaculis, ipsum. Sed aliquam ultrices mauris. Integer ante arcu, accumsan a, consectetuer eget, posuere ut, mauris. Praesent adipiscing. Phasellus ullamcorper. Duis arcu tortor, suscipit eget, imperdiet nec, imperdiet iaculis, ipsum.</div></div>
  <div class="foot">7</div>
</article>

<article class="slide c2" style="top:1511px">
  <div class="photo" role="img" aria-label="Glass office tower seen from below, red toned" style="left:0;top:0;width:218px;height:302px;background:linear-gradient(135deg,#c57072,#8b3033)"></div>
  <div style="position:absolute;left:30px;top:132px;font-family:Oswald,sans-serif;font-weight:500;font-size:23px;color:#fff">Agenda</div>
  <span class="mark tr">GRITLINE</span>
  <div style="position:absolute;left:236px;top:76px;font-family:Oswald,sans-serif;font-size:9px;color:var(--ink)">Start</div>
  <div style="position:absolute;left:272px;top:76px;font-size:7px;color:var(--ink);font-weight:600">◷ 9h00</div>
  <div style="position:absolute;left:236px;top:158px;font-family:Oswald,sans-serif;font-size:9px;color:var(--ink)">Break</div>
  <div style="position:absolute;left:272px;top:158px;font-size:7px;color:var(--ink);font-weight:600">◷ 12h00</div>
  <svg style="position:absolute;left:320px;top:72px" width="220" height="190" viewBox="0 0 220 190">
    <line x1="5" y1="8" x2="5" y2="178" stroke="#d8b5b6" stroke-width="1"/>
    <g fill="#a83236"><circle cx="5" cy="8" r="3.5"/><circle cx="5" cy="35" r="3.5"/><circle cx="5" cy="63" r="3.5"/><circle cx="5" cy="90" r="3.5"/><circle cx="5" cy="118" r="3.5"/><circle cx="5" cy="145" r="3.5"/><circle cx="5" cy="173" r="3.5"/></g>
    <g font-family="Open Sans, sans-serif" font-size="7" fill="#333">
      <text x="18" y="11">Lorem ipsum dolor sit amec</text><text x="18" y="38">Duis arcu tortor, suscipit eget.</text>
      <text x="18" y="66">Lorem ipsum dolor sit amec arcu tortor eget</text><text x="18" y="93">Duis arcu tortor, suscipit eget.</text>
      <text x="18" y="121">Duis arcu tortor.</text><text x="18" y="148">Duis arcu tortor, suscipit eget.</text>
      <text x="18" y="176">Lorem ipsum dolor sit amec arcu tortor eget</text></g>
  </svg>
  <div class="foot">4</div>
</article>

<!-- Row 4 -->
<article class="slide c1" style="top:1854px">
  <div class="title">About Us</div><span class="mark tr">GRITLINE</span>
  <div style="position:absolute;left:0;top:63px;width:226px;height:115px;background:var(--red)">
    <ul class="ticks wt" style="margin:33px 0 0 26px;font-size:6.5px;line-height:13px"><li>Duis arcu tortor, suscipit eget, imperdiet nec.</li><li>Sed aliquam ultrices mauris. Integer ante arcu.</li><li>Consectetuer eget, posuere ut, mauris.</li><li>Praesent adipiscing.</li></ul>
  </div>
  <div class="photo" role="img" aria-label="Winding road through a misty forest" style="left:226px;top:63px;width:334px;height:115px;background:linear-gradient(180deg,#5d6c6f,#28302f)"></div>
  <div style="position:absolute;left:26px;top:196px;width:508px"><div class="h">Replace Your Text Here</div><div class="p">Duis arcu tortor, suscipit eget, imperdiet nec, imperdiet iaculis, ipsum. Sed aliquam ultrices mauris. Integer ante arcu, accumsan a, consectetuer eget, posuere ut, mauris. Praesent adipiscing. Phasellus ullamcorper. Duis arcu tortor, suscipit eget, imperdiet nec, imperdiet iaculis, ipsum. Sed aliquam ultrices mauris. Integer ante arcu, accumsan a, consectetuer eget, posuere ut, mauris. Praesent adipiscing. Phasellus ullamcorper. Duis arcu tortor, suscipit eget, imperdiet nec, imperdiet iaculis, ipsum.</div></div>
  <div class="foot">8</div>
</article>

<article class="slide c2" style="top:1854px">
  <div class="title">Replace your text here</div><span class="mark tr">GRITLINE</span>
  <svg style="position:absolute;left:58px;top:66px" width="460" height="142" viewBox="0 0 460 142" role="img" aria-label="Three slanted photos: a desk with monitor, hands on a laptop, an empty office">
    <defs><linearGradient id="g1" x1="0" y1="0" x2="0" y2="1"><stop offset="0" stop-color="#d9d9d9"/><stop offset="1" stop-color="#4a4a4a"/></linearGradient>
    <linearGradient id="g2" x1="0" y1="0" x2="1" y2="1"><stop offset="0" stop-color="#f2f2f2"/><stop offset="1" stop-color="#9aa39a"/></linearGradient>
    <linearGradient id="g3" x1="0" y1="0" x2="0" y2="1"><stop offset="0" stop-color="#e6e6e6"/><stop offset="1" stop-color="#4f6a66"/></linearGradient></defs>
    <polygon points="20,0 140,0 120,142 0,142" fill="url(#g1)"/>
    <polygon points="170,0 290,0 270,142 150,142" fill="url(#g2)"/>
    <polygon points="320,0 440,0 420,142 300,142" fill="url(#g3)"/>
  </svg>
  <div style="position:absolute;top:220px;left:40px;width:480px;display:flex;justify-content:space-between;text-align:center">
    <div style="width:140px"><div class="h" style="margin-bottom:3px">Replace Your Text Here</div><div class="p" style="text-align:center">Imperdiet nec, imperdiet iaculis, ipsum. Lorem ipsum dolor.</div></div>
    <div style="width:140px"><div class="h" style="margin-bottom:3px">Replace Your Text Here</div><div class="p" style="text-align:center">Imperdiet nec, imperdiet iaculis, ipsum. Lorem ipsum.</div></div>
    <div style="width:140px"><div class="h" style="margin-bottom:3px">Replace Your Text Here</div><div class="p" style="text-align:center">Imperdiet nec, imperdiet iaculis, ipsum. Lorem ipsum.</div></div>
  </div>
  <div class="foot">14</div>
</article>

<!-- Row 5 -->
<article class="slide c1" style="top:2198px">
  <div class="title">Project Management</div><span class="mark tr">GRITLINE</span>
  <div style="position:absolute;left:26px;top:62px;width:260px"><div class="h">Replace Your Text Here</div><div class="p">Duis arcu tortor, suscipit eget, imperdiet nec, imperdiet iaculis, ipsum. Sed aliquam ultrices mauris. Integer ante arcu, accumsan a, consectetuer eget, posuere ut, mauris. Praesent adipiscing. Phasellus ullamcorper. Duis arcu tortor, suscipit eget, imperdiet nec, imperdiet iaculis, ipsum. Sed aliquam ultrices mauris. Integer ante arcu, accumsan a, consectetuer eget, posuere ut, mauris. Praesent adipiscing. Phasellus ullamcorper. Duis arcu tortor, suscipit eget, imperdiet nec, imperdiet iaculis, ipsum.<br><br>Duis arcu tortor, suscipit eget, imperdiet nec, imperdiet iaculis, ipsum. Sed aliquam ultrices mauris. Integer ante arcu, accumsan a, consectetuer eget, posuere ut, mauris.</div></div>
  <div class="photo" role="img" aria-label="Chalkboard planning grid with sticky notes" style="left:318px;top:64px;width:224px;height:214px;background:linear-gradient(135deg,#3a4144,#1f2426)"></div>
  <div class="foot">9</div>
</article>

<article class="slide c2" style="top:2198px">
  <div class="title">Project Management</div><span class="mark tr">GRITLINE</span>
  <div style="position:absolute;left:27px;top:62px;width:508px"><div class="h">Replace Your Text Here</div><div class="p">Duis arcu tortor, suscipit eget, imperdiet nec, imperdiet iaculis, ipsum. Sed aliquam ultrices mauris. Integer ante arcu, accumsan a, consectetuer eget, posuere ut, mauris. Praesent adipiscing. Phasellus ullamcorper. Duis arcu tortor, suscipit eget, imperdiet nec, imperdiet iaculis, ipsum. Sed aliquam ultrices mauris. Integer ante arcu, accumsan a, consectetuer eget, posuere ut, mauris. Praesent adipiscing. Phasellus ullamcorper. Duis arcu tortor, suscipit eget, imperdiet nec, imperdiet iaculis, consectetuer eget, posuere ut, mauris.<br><br><br>Duis arcu tortor, suscipit eget, imperdiet nec, imperdiet iaculis, ipsum. Sed aliquam ultrices mauris. Integer ante arcu, accumsan a, consectetuer eget, posuere ut, mauris. Duis arcu tortor, suscipit eget, imperdiet nec, imperdiet iaculis, ipsum. Sed aliquam ultrices mauris. Integer ante arcu, accumsan a, consectetuer eget, posuere ut, mauris. Praesent adipiscing. Phasellus ullamcorper. Duis arcu tortor, suscipit eget, imperdiet nec, imperdiet iaculis, ipsum. Sed aliquam ultrices mauris. Integer ante arcu, accumsan a, consectetuer eget, posuere ut, mauris.</div></div>
  <div class="foot">11</div>
</article>

<!-- Row 6 -->
<article class="slide c1" style="top:2541px">
  <div class="title">Replace your text here</div><span class="mark tr">GRITLINE</span>
  <div style="position:absolute;left:0;top:63px;width:560px;height:110px;background:linear-gradient(90deg,#9c4548,#8a2e31)">
    <div style="margin:20px 0 0 32px;width:500px"><div class="h wt">Replace Your Text Here</div><div class="p wt">Duis arcu tortor, suscipit eget, imperdiet nec, imperdiet iaculis, ipsum. Sed aliquam ultrices mauris. Integer ante arcu, accumsan a, consectetuer eget, posuere ut, mauris. Praesent adipiscing. Phasellus ullamcorper. Duis arcu tortor, suscipit eget, imperdiet nec, imperdiet iaculis, ipsum. Sed aliquam ultrices mauris.</div></div>
  </div>
  <div class="p" style="position:absolute;left:32px;top:198px;width:240px">Duis arcu tortor, suscipit eget, imperdiet nec, imperdiet iaculis, ipsum. Sed aliquam ultrices mauris. Integer ante arcu, accumsan a, consectetuer eget, posuere ut, mauris. Praesent adipiscing. Phasellus ullamcorper. Duis arcu tortor, suscipit eget, imperdiet nec, imperdiet iaculis, ipsum. Sed aliquam ultrices mauris.</div>
  <div class="p" style="position:absolute;left:297px;top:198px;width:240px">Duis arcu tortor, suscipit eget, imperdiet nec, imperdiet iaculis, ipsum. Sed aliquam ultrices mauris. Integer ante arcu, accumsan a, consectetuer eget, posuere ut, mauris. Praesent adipiscing. Phasellus ullamcorper. Duis arcu tortor, suscipit eget, imperdiet nec, imperdiet iaculis, ipsum. Sed aliquam ultrices mauris.</div>
  <div class="foot">15</div>
</article>

<article class="slide c2" style="top:2541px;background:linear-gradient(135deg,#b25b5d,#8b2e31 60%,#7a2326)">
  <div style="position:absolute;left:0;top:132px;width:560px;height:94px;background:#fff"></div>
  <div style="position:absolute;left:140px;top:132px;width:420px;height:94px;background:linear-gradient(90deg,#a9474a,#8c2f31)"></div>
  <span class="mark" style="position:absolute;left:30px;top:173px">GRITLINE</span>
  <div style="position:absolute;left:170px;top:146px;font-family:Oswald,sans-serif;font-weight:500;font-size:21px;color:#fff">01&nbsp;&nbsp;&nbsp;Section Slide</div>
  <div class="p wt" style="position:absolute;left:214px;top:178px;width:250px;font-size:6.5px;line-height:10px;text-align:left">Duis arcu tortor, suscipit eget, imperdiet nec, imperdiet iaculis, ipsum. Sed aliquam ultrices mauris. Integer ante arcu, accumsan a, consectetuer eget, posuere ut, mauris.</div>
</article>

<!-- Row 7 -->
<article class="slide c1" style="top:2886px">
  <div class="title">Replace your text here</div><span class="mark tr">GRITLINE</span>
  <div style="position:absolute;left:27px;top:58px;width:242px"><div class="h">Replace Your Text Here</div><div class="p">Duis arcu tortor, suscipit eget, imperdiet nec, imperdiet iaculis, ipsum. Sed aliquam ultrices mauris. Integer ante arcu, accumsan a, consectetuer eget, posuere ut, mauris. Praesent adipiscing. Phasellus ullamcorper. Duis arcu tortor, suscipit eget, imperdiet nec, imperdiet iaculis, ipsum. Sed aliquam ultrices mauris. Integer ante arcu, accumsan a, consectetuer eget, posuere ut, mauris. Praesent adipiscing. Phasellus ullamcorper. Duis arcu tortor, suscipit eget, imperdiet nec, imperdiet iaculis, ipsum.<br><br>Duis arcu tortor, suscipit eget, imperdiet nec, imperdiet iaculis, ipsum. Sed aliquam ultrices mauris. Integer ante arcu, accumsan a, consectetuer eget, posuere ut, mauris.</div></div>
  <div style="position:absolute;left:293px;top:58px;width:242px"><div class="h">Replace Your Text Here</div><div class="p">Duis arcu tortor, suscipit eget, imperdiet nec, imperdiet iaculis, ipsum. Sed aliquam ultrices mauris. Integer ante arcu, accumsan a, consectetuer eget, posuere ut, mauris. Praesent adipiscing. Phasellus ullamcorper. Duis arcu tortor, suscipit eget, imperdiet nec, imperdiet iaculis, ipsum. Sed aliquam ultrices mauris. Integer ante arcu, accumsan a, consectetuer eget, posuere ut, mauris. Praesent adipiscing. Phasellus ullamcorper. Duis arcu tortor, suscipit eget, imperdiet nec, imperdiet iaculis, ipsum.<br><br>Duis arcu tortor, suscipit eget, imperdiet nec, imperdiet iaculis, ipsum. Sed aliquam ultrices mauris. Integer ante arcu, accumsan a, consectetuer eget, posuere ut, mauris.</div></div>
  <div class="foot">12</div>
</article>

<article class="slide c2" style="top:2886px">
  <div class="title">Replace your text here</div><span class="mark tr">GRITLINE</span>
  <div style="position:absolute;left:38px;top:58px;width:480px;color:var(--grey)">
    <div class="h" style="margin-bottom:2px">Replace your text here</div>
    <ul class="ticks" style="margin-bottom:12px"><li>Duis arcu tortor, suscipit eget, imperdiet nec. Sed aliquam ultrices mauris. Integer ante arcu, accumsan</li><li>Sed aliquam ultrices mauris. Integer ante arcu, accumsan.</li><li>Consectetuer eget, posuere ut, mauris.</li></ul>
    <div class="h" style="margin-bottom:2px">Replace your text here</div>
    <ul class="ticks" style="margin-bottom:12px"><li>Duis arcu tortor, suscipit eget, imperdiet nec. Sed aliquam ultrices mauris. Integer ante arcu, accumsan</li><li>Sed aliquam ultrices mauris. Integer ante arcu, accumsan.</li><li>Consectetuer eget, posuere ut, mauris.</li></ul>
    <div class="h" style="margin-bottom:2px">Replace your text here</div>
    <ul class="ticks"><li>Duis arcu tortor, suscipit eget, imperdiet nec. Sed aliquam ultrices mauris. Integer ante arcu, accumsan</li><li>Sed aliquam ultrices mauris. Integer ante arcu, accumsan.</li><li>Consectetuer eget, posuere ut, mauris.</li></ul>
  </div>
  <div class="foot">13</div>
</article>

</body>
</html>
```